Inpatient and outpatient services for people who have undergone urinary and faecal diversions.
Rory Talbrick
Clinical Nurse Consultant Stomal Therapy
C/o K7f Surgical Unit
Carrowby Hospital
Carrowby 2318
P: 0413 587 240
P: 9731 2086 Pager: 63158
AS: 9731 4402 Clear writing and colour as people who read this may have vision problems
Information transfer about contact details, position of clinic, what to bring on follow up appointmants.

Target Market(s)

patients and staff to contact

Industry/Entity Type

Medical

Contact Information for Business Card

As above in Project description. Can use both sides.

Font styles to use
Decorative

Requirements
Must have
• Clear easy to read writing as patients may have eyesight problems
Nice to have
• Catchy colour & design

```html
<!DOCTYPE html>
<html lang="en">
<head>
<meta charset="utf-8">
<title>Rory Talbrick – Business Card</title>
<link rel="stylesheet" href="https://fonts.googleapis.com/css2?family=Lobster+Two:ital,wght@1,700&family=Arimo:wght@400&display=swap">
<style>
  :root {
    --backdrop: #e9e6e1;
    --charcoal: #2b2e30;
    --charcoal-deep: #1f2123;
    --black: #0b0b0c;
    --white: #ffffff;
    --sky: #2aa8dd;
    --ocean: #0f74b8;
    --accent-blue: #2ea3e3;
    --script: "Lobster Two", cursive;
    --sans: "Arimo", Arial, sans-serif;
  }
  * { box-sizing: border-box; margin: 0; padding: 0; }
  html, body { width: 1200px; height: 858px; overflow: hidden; }
  body {
    background: var(--backdrop);
    display: flex;
    align-items: center;
    justify-content: center;
    gap: 40px;
  }
  .card {
    position: relative;
    width: 540px;
    height: 330px;
    overflow: hidden;
    box-shadow: 0 10px 26px rgba(0,0,0,.25);
  }
  .card-shapes { position: absolute; inset: 0; }
  .name {
    font-family: var(--script);
    font-style: italic;
    font-weight: 700;
    color: var(--white);
    line-height: 1;
  }
  .role {
    font-family: var(--sans);
    color: var(--accent-blue);
    letter-spacing: .2px;
  }

  /* Front */
  .front .name { position: absolute; left: 34px; top: 70px; font-size: 42px; }
  .front .role { position: absolute; left: 34px; top: 128px; font-size: 15px; }
  .front .extra-lines {
    position: absolute; left: 120px; bottom: 48px;
    font-family: var(--sans); font-size: 14px; line-height: 1.45;
    color: var(--white);
  }
  .front .contact {
    position: absolute; right: 26px; top: 40px;
    font-family: var(--sans); font-size: 13.5px; line-height: 1.5;
    color: var(--white); text-align: right;
  }
  .contact-row { display: flex; justify-content: flex-end; align-items: center; gap: 8px; }
  .contact-icon { width: 14px; height: 14px; flex: none; }
  .address { margin-top: 4px; padding-right: 22px; }

  /* Back */
  .back { background: linear-gradient(160deg, #1a1a1c 0%, var(--black) 55%, #151517 100%); }
  .back .name { position: absolute; left: 0; right: 0; top: 110px; text-align: center; font-size: 54px; }
  .back .role { position: absolute; left: 0; right: 0; top: 186px; text-align: center; font-size: 19px; }
</style>
</head>
<body>

  <section class="card front" aria-label="Business card front">
    <svg class="card-shapes" viewBox="0 0 540 330" preserveAspectRatio="none" aria-hidden="true">
      <defs>
        <linearGradient id="blueSweep" x1="0" y1="0" x2="1" y2="1">
          <stop offset="0" stop-color="var(--sky)"/>
          <stop offset="1" stop-color="var(--ocean)"/>
        </linearGradient>
      </defs>
      <rect width="540" height="330" fill="url(#blueSweep)"/>
      <path d="M0 0 H348 C372 120 352 240 302 330 H0 Z" fill="var(--white)"/>
      <path d="M0 0 H252 C338 82 346 222 302 330 H0 Z" fill="var(--charcoal)"/>
    </svg>

    <h1 class="name">Rory Talbrick</h1>
    <p class="role">Clinical Nurse Consultant Stomal Therapy</p>

    <p class="extra-lines">Pager: 63158<br>AS: 9731 4402</p>

    <div class="contact">
      <div class="contact-row">0413 587 240
        <svg class="contact-icon" viewBox="0 0 14 14" aria-hidden="true"><rect width="14" height="14" rx="2" fill="var(--white)"/><rect x="4.5" y="2.5" width="5" height="9" rx="1" fill="var(--ocean)"/></svg>
      </div>
      <div class="contact-row">9731 2086
        <svg class="contact-icon" viewBox="0 0 14 14" aria-hidden="true"><rect width="14" height="14" rx="2" fill="var(--white)"/><path d="M4 3 L6 3 L6.8 5 L5.6 6 C6.2 7.4 6.8 8 8 8.6 L9 7.4 L11 8.2 L11 10 C7 10.5 3.5 7 4 3 Z" fill="var(--ocean)"/></svg>
      </div>
      <div class="contact-row">C/o K7f Surgical Unit
        <svg class="contact-icon" viewBox="0 0 14 14" aria-hidden="true"><rect width="14" height="14" rx="2" fill="var(--white)"/><path d="M7 2.5 C4.8 2.5 3.5 4 3.5 5.8 C3.5 8.2 7 11.5 7 11.5 C7 11.5 10.5 8.2 10.5 5.8 C10.5 4 9.2 2.5 7 2.5 Z" fill="var(--ocean)"/><circle cx="7" cy="5.8" r="1.3" fill="var(--white)"/></svg>
      </div>
      <div class="address">Carrowby Hospital<br>Carrowby 2318</div>
    </div>
  </section>

  <section class="card back" aria-label="Business card back">
    <h2 class="name">Rory Talbrick</h2>
    <p class="role">Clinical Nurse Consultant Stomal Therapy</p>
  </section>

</body>
</html>
```